Art startup needs 4 rotator images/banner ads for new website

DESIGN BRIEF
WHAT WE NEED: 4 Rotator images for homepage of new website
SIZE: 1000 width x 552 height
BACKDROPS: Lifestyle images, modern, simple, soft industrial settings. With large space to place artwork and text.
DESIGN: Not to look like Valto. Simple, chic setting, bold writing to convey key messages. Need to allow enough space for text to not be interrupted. Artwork and text needs to be primary focus, with chairs/table (lifestyle components) to be secondary.
Per attached notes: words in brackets ie [SHOP ARTWORK] need to included as a button on the rotator image. Ie to incentivize people to click on the button to be taken to a new page. Please refer to page 2 for existing example.
Please see attached for copy for each rotator image.
Have attached some examples of art. you don't need to include them, all, please select what you like to place insitu.

```html
<!DOCTYPE html>
<html lang="en">
<head>
<meta charset="utf-8">
<title>Homepage Rotator Banners</title>
<link rel="stylesheet" href="https://fonts.googleapis.com/css2?family=Oswald:wght@600;700&family=Roboto:wght@400&display=swap">
<style>
  :root {
    --stage: #3a2418;
    --orange: #e8702a;
    --orange-deep: #d85a1c;
    --button-edge: #3b2a22;
    --white: #ffffff;
    --ink: #111111;
    --teal-dark: #0d4a52;
    --teal: #1f8088;
    --night: #140d10;
    --wall: #e3e4e6;
    --brick: #d9d9d9;
  }
  * { box-sizing: border-box; margin: 0; padding: 0; }
  html, body { width: 1200px; height: 1000px; overflow: hidden; }
  body { background: var(--stage); position: relative; font-family: "Oswald", sans-serif; }

  .banner {
    position: absolute; width: 557px; height: 307px; overflow: hidden;
    box-shadow: 0 4px 14px rgba(0,0,0,.55);
  }
  .banner--campaign { left: 32px; top: 178px;
    background: radial-gradient(ellipse at 40% 40%, var(--teal) 0%, #17666e 50%, var(--teal-dark) 100%); }
  .banner--custom { left: 613px; top: 178px;
    background:
      linear-gradient(120deg, transparent 20%, rgba(110,30,50,.55) 30%, transparent 40%),
      linear-gradient(60deg, transparent 45%, rgba(90,120,60,.45) 55%, transparent 65%),
      linear-gradient(150deg, rgba(120,35,55,.5) 0%, var(--night) 45%, rgba(70,100,50,.4) 100%),
      var(--night); }
  .banner--limited { left: 32px; top: 515px;
    background: linear-gradient(180deg, #cfcfcf 0%, #f2f2f2 40%, #ececec 88%, #bdbdbd 90%, #d8d8d8 100%); }
  .banner--shop { left: 613px; top: 515px; }

  .photo { position: absolute; }
  .photo--child { right: 0; bottom: 0; width: 215px; height: 220px;
    background: linear-gradient(160deg, rgba(230,200,170,.0) 0%, rgba(230,215,200,.7) 40%, rgba(245,245,245,.85) 100%); }
  .photo--room { inset: 0;
    background: linear-gradient(180deg, #d5d6d9 0%, var(--wall) 70%, #c9a77c 82%, #e6e6e6 86%, #dcdcdc 100%); }
  .photo--painting { left: 337px; top: 22px; width: 196px; height: 239px;
    background: linear-gradient(180deg, #e88aa8 0%, #c96a78 35%, #f3b23c 65%, #f08fb0 100%);
    box-shadow: 2px 3px 6px rgba(0,0,0,.25); }

  .headline { position: absolute; color: var(--orange); font-weight: 700;
    text-transform: uppercase; letter-spacing: -0.5px; line-height: 1;
    text-shadow: 1px 2px 2px rgba(0,0,0,.45); }
  .headline--campaign { left: 0; right: 0; top: 50px; text-align: center; }
  .headline--campaign .line-1 { display: block; font-size: 26px; }
  .headline--campaign .line-2 { display: block; font-size: 36px; margin-top: 6px; }
  .headline--custom { left: 0; right: 0; top: 100px; text-align: center; font-size: 40px; }
  .headline--custom span { display: block; margin-bottom: 4px; }
  .headline--limited { left: 0; right: 0; top: 95px; text-align: center; font-size: 42px;
    color: var(--ink); text-shadow: 2px 3px 4px rgba(0,0,0,.45); }
  .headline--limited span { display: block; margin-bottom: 12px; }
  .headline--shop { left: 39px; top: 76px; font-size: 31px; text-shadow: none; }
  .headline--shop small { font-size: 23px; text-transform: none; font-weight: 600; }

  .cta { position: absolute; height: 28px; padding: 0 12px; display: flex; align-items: center;
    background: var(--orange-deep); border: 2px solid var(--button-edge);
    outline: 1px solid var(--orange); outline-offset: -4px;
    color: var(--white); font-family: "Roboto", sans-serif; font-size: 13px;
    text-transform: uppercase; white-space: nowrap;
    box-shadow: 1px 2px 3px rgba(0,0,0,.4); }
  .cta--campaign { left: 38px; top: 192px; }
  .cta--custom { left: 210px; top: 216px; }
  .cta--shop { left: 39px; top: 167px; height: 24px; font-size: 12px; padding: 0 8px; }
</style>
</head>
<body>
  <section class="banner banner--campaign">
    <div class="photo photo--child" role="img" aria-label="Young child painting at an easel"></div>
    <h2 class="headline headline--campaign">
      <span class="line-1">Your purchase provides a painting kit</span>
      <span class="line-2">to a disadvantaged youth</span>
    </h2>
    <a class="cta cta--campaign">Our children's campaign</a>
  </section>

  <section class="banner banner--custom" role="img" aria-label="Dark abstract brushstroke painting backdrop">
    <h2 class="headline headline--custom">
      <span>Custom painted for you.</span>
      <span>Delivered ready to hang</span>
    </h2>
    <a class="cta cta--custom">Free shipping</a>
  </section>

  <section class="banner banner--limited" role="img" aria-label="White brick wall with wooden floor">
    <h2 class="headline headline--limited">
      <span>This collection available</span>
      <span>for 14 days only</span>
    </h2>
  </section>

  <section class="banner banner--shop">
    <div class="photo photo--room" role="img" aria-label="Bright room with wooden table, cups, lemon bowl and chair"></div>
    <div class="photo photo--painting" role="img" aria-label="Pink and orange abstract painting on the wall"></div>
    <h2 class="headline headline--shop">Hand painted<br>art <small>from $199</small></h2>
    <a class="cta cta--shop">Shop artwork</a>
  </section>
</body>
</html>
```